A year in review booklet 12 page square mini booklet

a 12 page (including front and back cover) booklet 4.75 inches square.
Front Cover page (page 1)
Something that says WLGTC 2018 ministry year in review or something like that
Image of baptism/missions/etc
Intro Letter from Gordon (page 2) (text to be filled in later)
His headshot image (uploaded)
Quick note about year end giving (to be filled in later)
Sermon Listens (page 3)
Total # of sermon listens at the top (5800)
headphone icon
key at the bottom that says "headphone icon = X listens)
Try to fill most of the page with icons
Lantern Effort Houses Visited (pages 4 & 5)
Total # of houses visited at the top (23,899)
house icon
key at the bottom that says "house icon = 50? houses)
Babies Saved (page 6)
Total # of babies at the top (265)
baby icon
no key at the bottom make every baby = 1 icon
Tons of food served at Whitcombe Outreach (page 7)
Total # of food distributed at the top (500 tons)
bread loaf icon
key at the bottom that says "bread icon = 1 ton, 1000 lbs?, 100 lbs?)
Mission Trips Taken (pages 8&9)
Total # of mission trips taken at the top (11 trips)
airplane icon

Salvations (page 10)
Total # of salvations at the top (150 salvations)
cross icon
no key at the bottom make every salvation = 1 icon
Baptisms (page 11)
Total # of baptisms at the top 22
water droplet
no key at the bottom make every baptism = 1 icon

Back Cover page (page 12)
Give online shortlink (filled in later)
Give through month of December info

Target Market(s)

Church Congregation

Requirements
Must have
• Good graphics

```html
<!DOCTYPE html>
<html lang="en">
<head>
<meta charset="utf-8">
<title>WLGTC 2018 Year in Review – Cover</title>
<link href="https://fonts.googleapis.com/css2?family=Roboto:wght@400&display=swap" rel="stylesheet">
<style>
  :root {
    --photo-dark: #3a2a26;
    --photo-skin: #b8826c;
    --photo-shadow: #24222a;
    --basin-light: #e8e6e5;
    --basin-grey: #b3adaa;
    --basin-dark: #4a423e;
    --violet: #7663d2;
    --lavender: #bb90e8;
    --lavender-soft: #9b86e4;
    --mauve: #9c6fd6;
    --indigo: #5a49b4;
    --night: #3b3181;
    --text: #ffffff;
  }
  html, body {
    margin: 0;
    padding: 0;
    width: 1200px;
    height: 1200px;
    overflow: hidden;
    background: #ffffff;
  }
  .cover {
    position: relative;
    width: 1200px;
    height: 1200px;
    overflow: hidden;
  }
  .artwork {
    position: absolute;
    inset: 0;
    width: 1200px;
    height: 1200px;
    display: block;
  }
  .site-url {
    position: absolute;
    left: 334px;
    top: 612px;
    margin: 0;
    font-family: "Roboto", sans-serif;
    font-weight: 400;
    font-size: 77px;
    color: var(--text);
    line-height: 1;
    white-space: nowrap;
  }
</style>
</head>
<body>
  <main class="cover">
    <svg class="artwork" viewBox="0 0 1200 1200">
      <defs>
        <linearGradient id="photo-tone" x1="0" y1="0" x2="1" y2="1">
          <stop offset="0" stop-color="var(--photo-skin)"/>
          <stop offset="0.45" stop-color="var(--photo-dark)"/>
          <stop offset="1" stop-color="var(--photo-shadow)"/>
        </linearGradient>
        <linearGradient id="basin-tone" x1="0" y1="0" x2="0" y2="1">
          <stop offset="0" stop-color="var(--basin-dark)"/>
          <stop offset="0.35" stop-color="var(--basin-grey)"/>
          <stop offset="1" stop-color="var(--basin-light)"/>
        </linearGradient>
        <linearGradient id="lavender-band" x1="0" y1="1" x2="1" y2="0">
          <stop offset="0" stop-color="var(--lavender-soft)"/>
          <stop offset="0.55" stop-color="var(--lavender)"/>
          <stop offset="1" stop-color="var(--lavender)"/>
        </linearGradient>
      </defs>

      <!-- base violet field -->
      <rect class="band-base" width="1200" height="1200" fill="var(--violet)"/>

      <!-- light lavender band -->
      <path class="band-light" fill="url(#lavender-band)"
            d="M150,560 C400,470 760,470 1060,680 L1200,680 L1200,0 L1104,0 L700,240 Z"/>

      <!-- top right mauve corner -->
      <path class="band-corner" fill="var(--mauve)"
            d="M1104,0 C990,220 990,470 1050,690 L1200,672 L1200,0 Z"/>

      <!-- mid indigo band -->
      <path class="band-mid" fill="var(--indigo)"
            d="M0,1000 C260,880 560,760 820,700 C980,664 1100,660 1200,672 L1200,1200 L0,1200 Z"/>

      <!-- deep night lower right -->
      <path class="band-deep" fill="var(--night)"
            d="M648,984 C800,830 1000,710 1200,672 L1200,1200 L1040,1200 C940,1100 800,1010 648,984 Z"/>

      <!-- top-left photo with curved edge -->
      <path class="photo-baptism" role="img"
            aria-label="Photo of an infant being baptised as water is poured from a crystal pitcher over its head"
            fill="url(#photo-tone)"
            d="M0,0 L1104,0 Q552,296 0,768 Z"/>

      <!-- bottom basin photo -->
      <path class="photo-basin" role="img"
            aria-label="Photo of a white baptismal basin holding water"
            fill="url(#basin-tone)"
            d="M0,980 C160,958 420,970 640,1030 C820,1080 940,1140 1032,1200 L0,1200 Z"/>
    </svg>

    <p class="site-url">www.wlgtc2018.com</p>
  </main>
</body>
</html>
```